Harbor Lane PEO - Web Build for Professional Employment Organization

We need a website built for our new PEO (professional employment organization). This company will offer third party Human Resource services to companies who are looking to outsource:<br/>Recruiting<br/>Administrative Onboarding<br/>New hire training, ongoing training and development<br/>Payroll/compensation processing/services<br/>Employee Relations<br/>Unemployment Claim Facilitation<br/>Benefits Plans and Administration<br/><br/>I have attached the logo below. Please use that as a reference and color match as best as possible. <br/><br/>Here are some of the competitor's websites:<br/>https://www.workvantrix.com/ <br/>https://www.staffmerola.com/<br/>https://www.staffmerola.com/<br/>https://www.qlr.com/<br/>https://www.hirebendora.com/<br/>https://corvalpeo.com/contact-corval/<br/><br/>

Target Market(s)

Startups and mid-sized businesses

Number of Pages Required

5+ page

Font styles to use
Sans Serif

Colors
0592cd

Requirements
Must have
• Features Pages
• SEO driven keyword rich content
• Strong focus on our ability to provide unemployment claim facilitation services as well as mandatory training/certification fulfillment
Nice to have
• I'd like to see one mockup with a Live Chat version if possible. In theory, the Live Chat messages would go directly to our front desk person.

```html
<!DOCTYPE html>
<html lang="en">
<head>
<meta charset="utf-8">
<title>Harbor Lane PEO</title>
<link rel="stylesheet" href="https://fonts.googleapis.com/css2?family=Roboto:wght@300;400;500;700;900&display=swap">
<style>
:root{
  --teal:#1ba3bf;
  --teal-dark:#1792ab;
  --slate:#3f4a63;
  --slate-btn:#4a5670;
  --stats:#5f6f8d;
  --ink:#2f3a52;
  --text:#555b66;
  --muted:#8a9099;
  --line:#dfe3e8;
  --footer:#363738;
  --white:#fff;
}
*{box-sizing:border-box;margin:0;padding:0}
html,body{width:1200px;height:4870px;overflow:hidden}
body{font-family:'Roboto',sans-serif;color:var(--text);background:var(--white);position:relative}
.abs{position:absolute}
a{color:inherit;text-decoration:none}

/* header */
.site-header{position:absolute;top:0;left:0;width:1200px;height:95px;background:var(--white)}
.brand{position:absolute;left:160px;top:26px;display:flex;align-items:center;gap:10px}
.brand-mark{width:14px;height:14px;background:var(--teal);border-radius:50%}
.brand-name{font-size:28px;font-weight:500;color:var(--slate);letter-spacing:.5px}
.main-nav{position:absolute;top:38px;left:548px;display:flex;gap:0;font-size:13px;color:#333;font-weight:500}
.main-nav a{margin-right:34px}

/* hero */
.hero{position:absolute;top:95px;left:0;width:1200px;height:702px;background:linear-gradient(100deg,#2e3a55 0%,#46546f 45%,#5a6680 75%,#2f3b54 100%)}
.hero-title{position:absolute;left:158px;top:230px;font-size:44px;font-weight:700;color:var(--white);line-height:58px}
.hero-text{position:absolute;left:158px;top:380px;width:430px;font-size:14px;line-height:19px;color:var(--white)}
.btn-light{position:absolute;left:158px;top:487px;width:158px;height:52px;background:var(--white);color:var(--slate);font-size:11px;font-weight:700;display:flex;align-items:center;justify-content:center;letter-spacing:.3px}
.callback{position:absolute;left:675px;top:87px;width:458px;height:548px;background:#f8f8f9}
.callback h2{position:absolute;top:57px;width:100%;text-align:center;font-size:24px;color:var(--slate);font-weight:700}
.callback .sub{position:absolute;top:92px;width:100%;text-align:center;font-size:11px;color:var(--muted)}
.toggle{position:absolute;top:133px;left:75px;width:225px;height:37px;display:flex;border:1px solid var(--line);background:var(--white)}
.toggle span{flex:1;display:flex;align-items:center;justify-content:center;font-size:11px;color:#444}
.toggle .on{background:#e8e9ec}
.field{position:absolute;left:47px;width:282px;height:46px;border:1px solid var(--line);background:var(--white);font-size:11px;color:#aaa;padding:16px 18px}
.btn-dark{position:absolute;left:47px;top:447px;width:282px;height:49px;background:var(--slate-btn);color:var(--white);font-size:11px;font-weight:700;display:flex;align-items:center;justify-content:center}

/* section headings */
.eyebrow{position:absolute;width:1200px;text-align:center;font-size:12px;color:var(--ink);font-weight:500}
.eyebrow.teal{color:var(--teal)}
.sec-title{position:absolute;width:1200px;text-align:center;font-size:36px;font-weight:700;color:var(--ink)}
.sec-title em{font-style:normal;color:var(--teal)}
.sec-sub{position:absolute;width:1200px;text-align:center;font-size:15px;color:var(--text)}

/* services */
.service-card{position:absolute;width:209px;height:189px;background:var(--white);box-shadow:0 2px 8px rgba(0,0,0,.13);text-align:center}
.service-card svg{position:absolute;left:67px;top:38px}
.service-card p{position:absolute;bottom:22px;width:100%;font-size:11px;font-weight:500;color:#333;line-height:14px}

/* about */
.about{position:absolute;top:1478px;left:0;width:1200px;height:572px;background:linear-gradient(90deg,#d9dadc 0%,#ececed 40%,#f4f4f5 100%)}
.photo{display:block}
.quote-box{position:absolute;left:198px;top:399px;width:339px;height:126px;background:var(--teal);color:var(--white);padding:18px 46px}
.quote-box p{font-size:14px;line-height:18px}
.quote-box b{display:block;margin-top:22px;font-size:12px}
.quote-box small{font-size:10px}
.about-title{position:absolute;left:604px;top:112px;font-size:36px;font-weight:700;color:var(--slate);line-height:38px}
.about-text{position:absolute;left:604px;width:410px;font-size:10.5px;line-height:14px;color:#666}
.vision{position:absolute;left:609px;top:365px;width:434px;height:140px;background:var(--slate-btn);color:var(--white);padding:36px 20px 0 106px}
.vision h3{font-size:17px;font-weight:500}
.vision p{font-size:10px;line-height:13px;margin-top:8px}
.vision svg{position:absolute;left:16px;top:28px}
.vision-tail{position:absolute;left:645px;top:505px;width:0;height:0;border-left:0 solid transparent;border-right:26px solid transparent;border-top:30px solid var(--slate-btn)}

/* courses */
.course{position:absolute;top:2237px;width:280px;height:327px}
.course .img{height:187px}
.course .tag{position:absolute;left:12px;top:24px;background:var(--white);font-size:10px;color:#555;padding:3px 10px}
.course .body{height:140px;background:var(--teal);color:var(--white);text-align:center;padding:24px 30px 0}
.course .body p{font-size:13px;line-height:19px}
.course .price{margin-top:14px;font-size:22px}
.course .price small{font-size:10px}

/* stats */
.stats{position:absolute;top:2642px;left:0;width:1200px;height:340px;background:var(--stats)}
.stat{position:absolute;top:132px;display:flex;align-items:center;gap:14px;color:var(--white)}
.stat b{display:block;font-size:38px;font-weight:700;line-height:40px}
.stat small{font-size:10.5px;font-weight:500}

/* testimonials */
.testimonials{position:absolute;top:2982px;left:0;width:1200px;height:683px;background:linear-gradient(180deg,#e6e6e7,#f2f2f3)}
.t-box{position:absolute;top:191px;height:165px;background:#f0f0f1;box-shadow:0 2px 8px rgba(0,0,0,.12);padding:48px 30px 0 54px;font-size:14px;line-height:25px;color:#444}
.t-box .mark{position:absolute;left:22px;top:18px;font-size:48px;font-family:Georgia,serif;color:#333;line-height:1}
.t-name{position:absolute;top:390px;font-size:12px;font-style:italic;font-weight:700;color:#222}

/* blog */
.post{position:absolute;top:3878px;width:280px;height:392px;background:var(--white);box-shadow:0 2px 8px rgba(0,0,0,.13)}
.post .img{height:205px}
.post h3{margin:24px 12px 0;font-size:14px;font-weight:400;color:#333;line-height:19px}
.post p{margin:14px 16px 0;font-size:10px;line-height:13px;color:#666}
.post .date{position:absolute;left:16px;bottom:26px;font-size:8px;color:#777}
.post .more{position:absolute;right:22px;bottom:16px;width:115px;height:31px;border:1px solid #555;border-radius:16px;font-size:9px;color:#333;display:flex;align-items:center;justify-content:center}

/* footer */
.site-footer{position:absolute;top:4325px;left:0;width:1200px;height:513px;background:var(--footer);color:var(--white)}
.f-head{position:absolute;font-size:13px;font-weight:700}
.f-input{position:absolute;background:var(--white);font-size:10px;color:#999;padding:0 14px;display:flex;align-items:center}
.f-btn{position:absolute;background:var(--teal);font-size:10px;font-weight:700;display:flex;align-items:center;justify-content:center}
.f-list{position:absolute;list-style:none;font-size:11px;line-height:26px}
.f-list li::before{content:"›";color:var(--teal);margin-right:10px}
.social{position:absolute;left:538px;top:124px;display:flex;gap:9px}
.social span{width:16px;height:16px;border-radius:50%;background:var(--white)}
.copyright{position:absolute;top:4838px;left:0;width:1200px;height:32px;background:var(--teal);color:var(--white);font-size:11px;display:flex;align-items:center;justify-content:center}
</style>
</head>
<body>

<header class="site-header">
  <div class="brand"><span class="brand-mark"></span><span class="brand-name">Harbor Lane PEO</span></div>
  <nav class="main-nav"><a href="#">Home</a><a href="#">About Us</a><a href="#">Features</a><a href="#">Online Courses</a><a href="#">Blog</a><a href="#">Contact Us</a></nav>
</header>

<section class="hero" role="img" aria-label="Business team meeting around a table, blue-toned photo">
  <h1 class="hero-title">WELCOME TO<br>HARBOR LANE PEO</h1>
  <p class="hero-text">Lorem ipsum dolor sit amet, consectetur adipiscing elit, sed do eiusmod tempor incididunt ut labore et dolore magna aliqua. Ut enim ad minim veniam, quis nostrud exercitation.</p>
  <a class="btn-light" href="#">LEARN MORE</a>
  <form class="callback">
    <h2>Request For Call Back</h2>
    <div class="sub">Building Careers.Building Organisations</div>
    <div class="toggle"><span class="on">Employer</span><span>Job Seeker</span></div>
    <div class="field" style="top:194px">Name</div>
    <div class="field" style="top:256px">Email</div>
    <div class="field" style="top:318px">Company Name</div>
    <div class="field" style="top:380px">Enquiry About</div>
    <div class="btn-dark">SUBMITE NOW</div>
  </form>
</section>

<section class="services">
  <div class="eyebrow" style="top:886px">OUR SERVICES</div>
  <h2 class="sec-title" style="top:910px">HOW WE <em>CAN HELP YOU</em></h2>
  <p class="sec-sub" style="top:960px">Lorem ipsum dolor sit amet, consectetur adipiscing elit,</p>

  <div class="service-card" style="left:158px;top:1018px">
    <svg width="75" height="75" viewBox="0 0 75 75" fill="none" stroke="#3f4a63" stroke-width="2"><circle cx="37" cy="37" r="30" stroke="#bfe6ef"/><rect x="20" y="22" width="22" height="30" rx="2"/><circle cx="46" cy="44" r="9" stroke="#1ba3bf"/><line x1="52" y1="50" x2="60" y2="58"/></svg>
    <p>Recruiting</p></div>
  <div class="service-card" style="left:383px;top:1018px">
    <svg width="75" height="75" viewBox="0 0 75 75" fill="none" stroke="#3f4a63" stroke-width="2"><circle cx="37" cy="37" r="30" stroke="#bfe6ef"/><rect x="20" y="20" width="35" height="34" rx="2"/><line x1="20" y1="29" x2="55" y2="29"/><rect x="25" y="34" width="6" height="5" stroke="#1ba3bf"/><rect x="35" y="34" width="6" height="5"/><rect x="45" y="34" width="6" height="5"/><rect x="25" y="43" width="6" height="5"/><rect x="35" y="43" width="6" height="5" stroke="#1ba3bf"/></svg>
    <p>Administrative<br>Onboarding</p></div>
  <div class="service-card" style="left:607px;top:1018px">
    <svg width="75" height="75" viewBox="0 0 75 75" fill="none" stroke="#3f4a63" stroke-width="2"><circle cx="37" cy="37" r="30" stroke="#bfe6ef"/><rect x="18" y="22" width="39" height="26" rx="2"/><line x1="30" y1="56" x2="45" y2="56"/><line x1="37" y1="48" x2="37" y2="56"/><circle cx="37" cy="32" r="5" stroke="#1ba3bf"/><path d="M29 45c2-5 14-5 16 0"/></svg>
    <p>New hire training, ongoing<br>training and development</p></div>
  <div class="service-card" style="left:832px;top:1018px">
    <svg width="75" height="75" viewBox="0 0 75 75" fill="none" stroke="#3f4a63" stroke-width="2"><circle cx="37" cy="37" r="30" stroke="#bfe6ef"/><circle cx="37" cy="26" r="7"/><path d="M24 48c2-10 24-10 26 0"/><circle cx="48" cy="46" r="8" stroke="#1ba3bf"/><rect x="18" y="40" width="12" height="14"/></svg>
    <p>Payroll/compensation<br>processing/services</p></div>

  <div class="service-card" style="left:158px;top:1226px">
    <svg width="75" height="75" viewBox="0 0 75 75" fill="none" stroke="#3f4a63" stroke-width="2"><circle cx="37" cy="37" r="30" stroke="#bfe6ef"/><circle cx="27" cy="28" r="6"/><circle cx="47" cy="28" r="6"/><path d="M17 48c2-9 18-9 20 0M37 48c2-9 18-9 20 0"/><path d="M30 54h14" stroke="#1ba3bf"/></svg>
    <p>Employee Relations</p></div>
  <div class="service-card" style="left:383px;top:1226px">
    <svg width="75" height="75" viewBox="0 0 75 75" fill="none" stroke="#3f4a63" stroke-width="2"><circle cx="37" cy="37" r="30" stroke="#bfe6ef"/><circle cx="28" cy="26" r="6"/><path d="M18 52c1-12 19-12 20 0"/><circle cx="48" cy="38" r="9" stroke="#1ba3bf"/><line x1="54" y1="45" x2="60" y2="52"/></svg>
    <p>Unemployment<br>Claim Facilitation</p></div>
  <div class="service-card" style="left:607px;top:1226px">
    <svg width="75" height="75" viewBox="0 0 75 75" fill="none" stroke="#3f4a63" stroke-width="2"><circle cx="37" cy="37" r="30" stroke="#bfe6ef"/><circle cx="34" cy="40" r="13"/><path d="M34 40V27M34 40h13" stroke="#1ba3bf"/><path d="M44 24l12-6 -2 10"/></svg>
    <p>Benefits Plans</p></div>
  <div class="service-card" style="left:832px;top:1226px">
    <svg width="75" height="75" viewBox="0 0 75 75" fill="none" stroke="#3f4a63" stroke-width="2"><circle cx="37" cy="37" r="30" stroke="#bfe6ef"/><path d="M17 30L37 18l20 12z"/><line x1="23" y1="33" x2="23" y2="50"/><line x1="32" y1="33" x2="32" y2="50"/><line x1="42" y1="33" x2="42" y2="50"/><line x1="51" y1="33" x2="51" y2="50"/><line x1="16" y1="54" x2="58" y2="54" stroke="#1ba3bf"/></svg>
    <p>Administration</p></div>
</section>

<section class="about">
  <div class="abs photo" style="left:198px;top:85px;width:339px;height:287px;background:linear-gradient(135deg,#9aa3ad,#c9ced4 60%,#e3e6ea)" role="img" aria-label="Smiling businessman in a grey suit giving a thumbs up"></div>
  <div class="quote-box">
    <p>Sed do eiusmod tempor incididunt ut labore et dolore magna aliqua.</p>
    <b>Marc Ellory</b><small>CEO &amp; Founder</small>
  </div>
  <div class="abs eyebrow teal" style="left:607px;top:84px;width:auto;text-align:left">ABOUT US</div>
  <h2 class="about-title">WHAT IS HARBOR<br>LANE PEO</h2>
  <p class="about-text" style="top:217px">Lorem ipsum dolor sit amet, consectetur adipiscing elit, sed do eiusmod tempor incididunt ut labore et dolore magna aliqua. Ut enim ad minim veniam, quis nostrud exercitation ullamco laboris nisi ut aliquip ex ea commodo consequat.</p>
  <p class="about-text" style="top:277px">Duis aute irure dolor in reprehenderit in voluptate velit esse cillum dolore eu fugiat nulla pariatur. Excepteur sint occaecat cupidatat non proident, sunt in culpa qui officia deserunt mollit anim id est laborum.</p>
  <div class="vision">
    <svg width="78" height="78" viewBox="0 0 78 78" fill="none" stroke="#fff" stroke-width="2.5"><circle cx="36" cy="40" r="28"/><circle cx="36" cy="40" r="18"/><circle cx="36" cy="40" r="8"/><line x1="36" y1="40" x2="66" y2="10"/><path d="M60 10h6v6"/></svg>
    <h3>Vision Statement</h3>
    <p>Ut enim ad minim veniam, quis nostrud exercitation ullamco laboris nisi ut aliquip ex ea commodo consequat.</p>
  </div>
  <div class="vision-tail"></div>
</section>

<section class="courses">
  <div class="eyebrow" style="top:2121px">COURSES</div>
  <h2 class="sec-title" style="top:2146px;color:var(--teal-dark)">ONLINE COURSES</h2>
  <div class="course" style="left:158px">
    <div class="img" role="img" aria-label="Rising arrow over a financial chart" style="background:linear-gradient(135deg,#1d3a7a,#5a86c8)"></div>
    <span class="tag">MOTIVATION</span>
    <div class="body"><p>Lorem ipsum dolor sit amet, consectetur adipiscing elit, sed do.</p><div class="price">$80 <small>/Month</small></div></div>
  </div>
  <div class="course" style="left:460px">
    <div class="img" role="img" aria-label="Handshake in front of a city skyline" style="background:linear-gradient(180deg,#3a6fb8,#17345e)"></div>
    <span class="tag">MARKETING</span>
    <div class="body"><p>Ut enim ad minim veniam, quis nostrud exercitatio</p><div class="price">Free!</div></div>
  </div>
  <div class="course" style="left:760px">
    <div class="img" role="img" aria-label="Team working with papers at a desk" style="background:linear-gradient(135deg,#2a3f70,#c9ccd3)"></div>
    <span class="tag">TEAM BUILDING</span>
    <div class="body"><p>Sed do eiusmod tempor incididunt ut labore et dolore magna aliqua.</p><div class="price">$100 <small>/Month</small></div></div>
  </div>
</section>

<section class="stats">
  <div class="stat" style="left:140px">
    <svg width="38" height="50" viewBox="0 0 38 50" fill="none" stroke="#fff" stroke-width="2"><rect x="2" y="2" width="34" height="46" rx="3"/><line x1="9" y1="13" x2="29" y2="13"/><line x1="9" y1="21" x2="29" y2="21"/><line x1="9" y1="29" x2="29" y2="29"/><line x1="9" y1="37" x2="22" y2="37"/></svg>
    <div><b>890+</b><small>JOBS AVAILABLE</small></div></div>
  <div class="stat" style="left:372px">
    <svg width="38" height="50" viewBox="0 0 38 50" fill="none" stroke="#fff" stroke-width="2"><path d="M2 2h24l10 10v36H2z"/><circle cx="19" cy="24" r="6"/><path d="M9 40c2-8 18-8 20 0"/></svg>
    <div><b>3120+</b><small>ACTIVE RESUMES</small></div></div>
  <div class="stat" style="left:598px">
    <svg width="46" height="46" viewBox="0 0 46 46" fill="none" stroke="#fff" stroke-width="2"><rect x="2" y="12" width="28" height="22" rx="2"/><circle cx="14" cy="21" r="4"/><circle cx="35" cy="30" r="8"/><line x1="8" y1="40" x2="24" y2="40"/></svg>
    <div><b>230+</b><small>EMPLOYERS PROFILES</small></div></div>
  <div class="stat" style="left:835px">
    <svg width="46" height="46" viewBox="0 0 46 46" fill="none" stroke="#fff" stroke-width="2"><circle cx="23" cy="23" r="20"/><path d="M13 24l7 7 13-15"/></svg>
    <div><b>150+</b><small>POSITIONS MATCHED</small></div></div>
</section>

<section class="testimonials">
  <div class="eyebrow teal" style="top:101px">TESTIMONIALS</div>
  <h2 class="sec-title" style="top:120px">What Our <em>Happy Clients</em> Say</h2>
  <blockquote class="t-box" style="left:158px;width:363px"><span class="mark">“</span>Lorem ipsum dolor sit amet, consectetur adipiscing elit, sed do eiusmod tempor incididunt ut labore et dolore magna aliqua. ”</blockquote>
  <blockquote class="t-box" style="left:611px;width:430px"><span class="mark">“</span>Lorem ipsum dolor sit amet, consectetur adipiscing elit, sed do eiusmod tempor incididunt ut labore et dolore magna aliqua. ”</blockquote>
  <div class="t-name" style="left:255px">Tessa Marlow</div>
  <div class="t-name" style="left:866px">Nina Calder</div>
  <div class="abs" style="left:5px;top:408px;width:1190px;height:275px;background:linear-gradient(180deg,rgba(150,150,150,.25),#8c8c8c 60%,#6e6e6e)" role="img" aria-label="Row of people holding laptops, tablets and phones, greyscale photo"></div>
</section>

<section class="blog">
  <div class="eyebrow teal" style="top:3763px">OUR BLOG</div>
  <h2 class="sec-title" style="top:3785px">LATEST NEWS <em>AND EVENTS</em></h2>
  <article class="post" style="left:158px">
    <div class="img" role="img" aria-label="Hands signing papers at a desk with coffee" style="background:linear-gradient(135deg,#5b4636,#b9a58e)"></div>
    <h3>LOREM IPSUM DOLOR SIT CONSECTETUR</h3>
    <p>Lorem ipsum dolor sit amet, consectetur adipiscing elit, sed do eiusmod tempor incididunt...</p>
    <span class="date">05 JAN 2020</span><a class="more" href="#">READ MORE</a>
  </article>
  <article class="post" style="left:460px">
    <div class="img" role="img" aria-label="Presenter at a whiteboard with sticky notes" style="background:linear-gradient(135deg,#8e7a66,#e4e1da)"></div>
    <h3>LOREM IPSUM DOLOR SIT CONSECTETUR</h3>
    <p>Lorem ipsum dolor sit amet, consectetur adipiscing elit, sed do eiusmod tempor incididunt...</p>
    <span class="date">05 JAN 2020</span><a class="more" href="#">READ MORE</a>
  </article>
  <article class="post" style="left:760px">
    <div class="img" role="img" aria-label="Desktop monitor on a desk in an office" style="background:linear-gradient(135deg,#c96a4f,#e7d8ce)"></div>
    <h3>LOREM IPSUM DOLOR SIT CONSECTETUR</h3>
    <p>Lorem ipsum dolor sit amet, consectetur adipiscing elit, sed do eiusmod tempor incididunt...</p>
    <span class="date">05 JAN 2020</span><a class="more" href="#">READ MORE</a>
  </article>
</section>

<footer class="site-footer">
  <div class="f-head" style="left:158px;top:80px">Subscribe Our Newsletter</div>
  <div class="f-input" style="left:158px;top:113px;width:200px;height:38px;padding-left:30px">Enter Your Email</div>
  <div class="f-btn" style="left:358px;top:113px;width:86px;height:38px">SUBSCRIBE</div>
  <div class="f-head" style="left:567px;top:92px">Follow Us</div>
  <div class="social" aria-label="Social links"><span></span><span></span><span></span><span></span><span></span></div>
  <div class="f-head" style="left:760px;top:80px">Need Help ?</div>
  <div class="abs" style="left:765px;top:118px;font-size:13px;font-weight:700;display:flex;align-items:center;gap:10px">
    <svg width="13" height="13" viewBox="0 0 24 24" fill="#fff"><path d="M6.6 10.8a15 15 0 006.6 6.6l2.2-2.2c.3-.3.7-.4 1-.2 1.1.4 2.3.6 3.6.6.6 0 1 .4 1 1V20c0 .6-.4 1-1 1A17 17 0 013 4c0-.6.4-1 1-1h3.5c.6 0 1 .4 1 1 0 1.3.2 2.5.6 3.6.1.3 0 .7-.2 1z"/></svg>
    CALL US : +0 555 210 4478</div>
  <div class="abs" style="left:158px;top:212px;width:905px;height:1px;background:#555"></div>

  <div class="f-head" style="left:158px;top:245px">About Us</div>
  <p class="abs" style="left:158px;top:277px;width:210px;font-size:9.5px;line-height:12px;color:#ddd">Lorem ipsum dolor sit amet, consectetur adipiscing elit, sed do eiusmod tempor incididunt ut labore et dolore magna aliqua. Ut enim ad minim veniam, quis nostrud exercitation ullamco laboris nisi ut aliquip ex ea commodo consequat. Duis aute irure dolor in reprehenderit in voluptate velit esse cillum dolore eu fugiat nulla pariatur. Excepteur sint occaecat cupidatat non proident, sunt in culpa qui officia deserunt mollit anim id est laborum.</p>

  <div class="f-head" style="left:452px;top:245px">Company</div>
  <ul class="f-list" style="left:460px;top:268px"><li>Home</li><li>About Us</li><li>Features</li><li>Blog</li><li>Contact Us</li></ul>
  <div class="f-head" style="left:609px;top:245px">Quick Links</div>
  <ul class="f-list" style="left:616px;top:268px"><li>How It Works</li><li>Add Listing</li><li>Popular Categories</li><li>Popular Places</li><li>FAQ</li></ul>
  <div class="f-head" style="left:768px;top:245px">Get In Touch</div>
  <div class="f-input" style="left:768px;top:272px;width:287px;height:36px">Enter Your Name</div>
  <div class="f-input" style="left:768px;top:318px;width:287px;height:36px">Enter Your Email</div>
  <div class="f-input" style="left:768px;top:364px;width:200px;height:36px">Enter Your Message</div>
  <div class="f-btn" style="left:968px;top:364px;width:87px;height:36px">SUBSCRIBE</div>
</footer>
<div class="copyright">Copyright © 2020 Harbor Lane PEO.All Rights Reserved.</div>

</body>
</html>
```